Torvane PT Business Card

I need the card to be bright/bold colours to stand out amongst others.
It needs to have my company logo.
I was not interested in pictures etc just a layout that attracts attention.

I have attached my old design which is very plain. I also needed change the contact details. And my description changed to Personal Trainer
Phone 0427391058
Facebook Torvane PT
No email address please, no street address.
And only Torvane PT (Please remove anything to do with Torvane Supplements)

```html
<!DOCTYPE html>
<html lang="en">
<head>
<meta charset="utf-8">
<title>Torvane PT Business Card</title>
<link href="https://fonts.googleapis.com/css2?family=Saira+Semi+Condensed:wght@400;500;600;700&display=swap" rel="stylesheet">
<style>
  :root {
    --page-bg: #e8eaed;
    --card-white: #fbfbfc;
    --teal-dark: #1d7a9c;
    --teal-light: #2f95b8;
    --stripe-blue: #2a8fd2;
    --sunny-yellow: #f8e34c;
    --amber: #f6b82c;
    --amber-light: #f9cb3c;
    --ink-blue: #1f7fbf;
    --ink-dark: #24445a;
    --brand-yellow: #f2c916;
    --divider: #5aa6d6;
  }
  * { box-sizing: border-box; margin: 0; padding: 0; }
  html, body {
    width: 1200px; height: 1200px; overflow: hidden;
    background: var(--page-bg);
    font-family: "Saira Semi Condensed", "Arial Narrow", sans-serif;
  }
  .business-card {
    position: absolute; left: 50px; top: 267px;
    width: 1100px; height: 666px;
    background: var(--card-white);
    overflow: hidden;
    box-shadow: 0 10px 30px rgba(30,50,70,.18);
  }
  .card-shapes { position: absolute; inset: 0; }
  .brand-name {
    position: absolute; left: 82px; top: 296px;
    font-size: 68px; font-weight: 700; letter-spacing: 2px;
    color: var(--brand-yellow); line-height: 1; white-space: nowrap;
  }
  .contact-block {
    position: absolute; right: 44px; top: 246px;
    width: 480px;
    text-align: right;
  }
  .holder-line {
    font-size: 32px; font-weight: 700; color: var(--ink-blue);
    letter-spacing: 1px; margin-right: 50px; margin-bottom: 30px;
    white-space: nowrap; line-height: 1.2;
  }
  .holder-line .role { font-size: 22px; font-weight: 500; letter-spacing: 0; }
  .contact-row {
    display: flex; align-items: center; justify-content: flex-end;
    gap: 14px; height: 54px;
    font-size: 25px; font-weight: 500; color: var(--ink-dark);
    white-space: nowrap;
  }
  .contact-row.social { font-weight: 700; }
  .contact-icon { width: 36px; height: 36px; flex: none; }
</style>
</head>
<body>
  <div class="business-card">
    <svg class="card-shapes" viewBox="0 0 1100 666" width="1100" height="666" aria-hidden="true">
      <defs>
        <linearGradient id="tealTop" x1="0" y1="0" x2="1" y2="0">
          <stop offset="0" stop-color="var(--teal-dark)"/>
          <stop offset="1" stop-color="var(--teal-light)"/>
        </linearGradient>
        <linearGradient id="amberBase" x1="0" y1="0" x2="0" y2="1">
          <stop offset="0" stop-color="var(--amber-light)"/>
          <stop offset="1" stop-color="var(--amber)"/>
        </linearGradient>
      </defs>
      <path class="top-shadow" d="M0,128 Q560,190 1100,88 V100 Q560,206 0,140 Z" fill="#d9dde2"/>
      <path class="top-band" d="M0,0 H1100 V86 Q560,184 0,120 Z" fill="url(#tealTop)"/>
      <path class="top-stripe" d="M0,152 Q560,215 1100,62 V104 Q560,240 0,174 Z" fill="var(--stripe-blue)"/>
      <path class="bottom-shadow" d="M0,592 Q560,530 1100,596 V606 Q560,544 0,604 Z" fill="#e2e4e7"/>
      <path class="bottom-stripe" d="M0,566 Q560,508 1100,576 V590 Q560,524 0,582 Z" fill="var(--sunny-yellow)"/>
      <path class="bottom-band" d="M0,612 Q560,540 1100,614 V666 H0 Z" fill="url(#amberBase)"/>
      <path class="divider" d="M561,262 V376 L569,384 L561,392 V504" fill="none" stroke="var(--divider)" stroke-width="2"/>
    </svg>

    <div class="brand-name">Torvane PT</div>

    <div class="contact-block">
      <div class="holder-line">DANE HOLLOWAY <span class="role">Personal Trainer</span></div>
      <div class="contact-row">0427391058
        <svg class="contact-icon" viewBox="0 0 36 36" aria-hidden="true"><circle cx="18" cy="18" r="17" fill="var(--ink-blue)"/><path d="M12 10l4 0 1.5 4.5-2.5 1.5a10 10 0 0 0 5 5l1.5-2.5 4.5 1.5v4a2 2 0 0 1-2 2A16 16 0 0 1 10 12a2 2 0 0 1 2-2z" fill="var(--brand-yellow)"/></svg>
      </div>
      <div class="contact-row social">Torvane PT
        <svg class="contact-icon" viewBox="0 0 36 36" aria-hidden="true"><circle cx="18" cy="18" r="17" fill="var(--ink-blue)"/></svg>
      </div>
    </div>
  </div>
</body>
</html>
```